Startup in search for creative and funky label for a food product

We, Vindmark Food Lab need a label for a new product: extra virgin oil from roasted sunflower seeds. The oil is produced at family gardens in sunny Kakheti region in Western Georgia.
Our goal is to introduce this new exclusive product, unknown in Western Europe. The test panels in Sweden liked the product and we hope to sell both for foodies and general public.
The feeling of the label shoud be both creative and exclusive. Maybe even funky, please see the file attached.

We would like to have the label in English and Swedish. Maybe we can do it in English first, since not all of you would understand Swedish, the Swedish design would be identical. The document below has both English and Swedish text.

We attachthe image of the bottle, please do not consider the label on the bottle, it is just an example.

Target Market(s)

General Market in Sweden and Europe. First priority: foddies, restaurants, specialized food stores.

Industry/Entity Type

Online Shopping

Requirements
Must have
• We would need the design in two languages, the same design for Swedish and English, but two separated labels. Once we agree on the English version, we can do the same for Swedish.
Nice to have
• Feeling of locally grown sunflowers, eye-catching.
Should not have
• Classic design for oil

```html
<!DOCTYPE html>
<html lang="en">
<head>
<meta charset="utf-8">
<title>Vindmark Food Lab – Sunflower Oil Label</title>
<link href="https://fonts.googleapis.com/css2?family=Oswald:wght@500&display=swap" rel="stylesheet">
<style>
  :root {
    --page-bg: #d9d9d9;
    --sky-top: #1a7fd0;
    --sky-mid: #6fb2e6;
    --sky-light: #eef5fb;
    --oil-light: #f6dc7a;
    --oil-gold: #e0b021;
    --oil-deep: #b7860c;
    --flower-orange: #f08a1c;
    --flower-yellow: #f9c623;
    --flower-white: #fbf6e6;
    --wave-yellow: #fcd12c;
    --wave-light: #fde27a;
    --badge-tan: #c79b6c;
    --badge-ink: #2b1d12;
    --title-green: #1e6b2c;
  }
  * { margin: 0; padding: 0; box-sizing: border-box; }
  html, body {
    width: 1023px;
    height: 1200px;
    overflow: hidden;
    background: var(--page-bg);
  }
  .label {
    position: absolute;
    left: 211px;
    top: 100px;
    width: 600px;
    height: 1000px;
    overflow: hidden;
  }
  .label-art {
    position: absolute;
    inset: 0;
    width: 600px;
    height: 1000px;
    display: block;
  }
  .brand-badge {
    position: absolute;
    left: 172px;
    top: 68px;
    width: 252px;
    height: 252px;
    border-radius: 50%;
    background: var(--badge-tan);
    display: flex;
    align-items: center;
    justify-content: center;
    text-align: center;
  }
  .brand-name {
    font-family: "Oswald", sans-serif;
    font-weight: 500;
    font-size: 34px;
    line-height: 1.1;
    color: var(--badge-ink);
    text-transform: uppercase;
    letter-spacing: 1px;
  }
  .product-title {
    position: absolute;
    left: 0;
    top: 358px;
    width: 600px;
    text-align: center;
    font-family: "Oswald", sans-serif;
    font-weight: 500;
    font-size: 42px;
    line-height: 65px;
    color: var(--title-green);
    text-transform: uppercase;
  }
</style>
</head>
<body>
  <main class="label">
    <svg class="label-art" viewBox="0 0 600 1000" xmlns="http://www.w3.org/2000/svg">
      <defs>
        <linearGradient id="skyGradient" x1="0" y1="0" x2="1" y2="1">
          <stop offset="0" stop-color="var(--sky-top)"/>
          <stop offset="0.55" stop-color="var(--sky-mid)"/>
          <stop offset="1" stop-color="var(--sky-light)"/>
        </linearGradient>
        <radialGradient id="oilGradient" cx="0.5" cy="0.5" r="0.5">
          <stop offset="0" stop-color="var(--oil-light)"/>
          <stop offset="0.6" stop-color="var(--oil-gold)"/>
          <stop offset="0.9" stop-color="var(--oil-deep)" stop-opacity="0.8"/>
          <stop offset="1" stop-color="var(--oil-deep)" stop-opacity="0"/>
        </radialGradient>
        <linearGradient id="flowerGradient" x1="0" y1="0" x2="1" y2="0">
          <stop offset="0" stop-color="var(--flower-orange)"/>
          <stop offset="0.2" stop-color="var(--flower-yellow)"/>
          <stop offset="0.35" stop-color="var(--flower-white)"/>
          <stop offset="0.5" stop-color="var(--flower-yellow)"/>
          <stop offset="0.65" stop-color="var(--flower-white)"/>
          <stop offset="0.85" stop-color="var(--flower-yellow)"/>
          <stop offset="1" stop-color="var(--flower-orange)"/>
        </linearGradient>
        <linearGradient id="waveGradient" x1="0" y1="0" x2="0" y2="1">
          <stop offset="0" stop-color="var(--wave-yellow)"/>
          <stop offset="1" stop-color="var(--wave-light)"/>
        </linearGradient>
      </defs>
      <rect class="sky-photo" x="0" y="0" width="600" height="1000" fill="url(#skyGradient)" role="img" aria-label="Photo of a bright blue sky with white clouds and sunlight"/>
      <ellipse class="oil-splash-photo" cx="300" cy="510" rx="320" ry="215" fill="url(#oilGradient)" role="img" aria-label="Photo of golden sunflower oil splashing"/>
      <path class="flowers-photo" d="M0,700 C30,665 80,655 120,680 C160,650 210,650 250,690 C290,670 320,655 360,665 C400,640 450,645 480,670 C520,650 570,650 600,665 L600,880 L0,880 Z" fill="url(#flowerGradient)" role="img" aria-label="Photo of yellow, orange and white daisy-like flowers"/>
      <path class="yellow-wave" d="M0,845 C140,790 250,835 380,795 S540,725 600,732 L600,1000 L0,1000 Z" fill="url(#waveGradient)"/>
    </svg>

    <div class="brand-badge">
      <span class="brand-name">Vindmark<br>Food Lab</span>
    </div>

    <h1 class="product-title">Extra virgin oil<br>from roasted<br>sunflower<br>seeds</h1>
  </main>
</body>
</html>
```